Keep Harbor Homes. Avoid short sale, foreclosure, repossession, negative credit inquires and all other negative actions associated with your real estate.

Call 844-27-LUMEN or info@keepharborhomes.example

```html
<!DOCTYPE html>
<html lang="en">
<head>
<meta charset="utf-8">
<title>Keep Harbor Homes — Postcard</title>
<link href="https://fonts.googleapis.com/css2?family=Oswald:wght@400;500;600&family=Lato:ital,wght@0,700;1,400&display=swap" rel="stylesheet">
<style>
  :root {
    --red: #d2302a;
    --red-dark: #a8221d;
    --navy: #1b3275;
    --blue: #1f4a9c;
    --blue-deep: #142a66;
    --white: #ffffff;
    --ink: #333333;
    --stage: #e9e9e9;
    --rule: #9a9a9a;
  }
  html, body { margin: 0; padding: 0; width: 902px; height: 1200px; overflow: hidden; background: var(--stage); }
  .stage { position: relative; width: 930px; height: 1237px; transform: scale(0.97); transform-origin: 0 0; }
  .card { position: absolute; background: var(--white); overflow: hidden; box-shadow: 0 3px 10px rgba(0,0,0,.25); }
  .card-front { left: 78px; top: 58px; width: 734px; height: 500px; }
  .card-back { left: 141px; top: 623px; width: 736px; height: 500px; }
  .shape-layer { position: absolute; inset: 0; }
  .headline-band { position: absolute; left: 0; top: 0; width: 100%; height: 114px; background: var(--red); }
  .headline { position: absolute; left: 42px; top: 14px; margin: 0; font: 500 70px/1 "Oswald", sans-serif; color: var(--white); letter-spacing: 0.5px; text-transform: uppercase; }
  .photo { position: absolute; }
  .front-photo {
    left: 0; top: 114px; width: 470px; height: 340px;
    background: linear-gradient(180deg, #c9d3e2 0%, #b9a98b 55%, #6f8f45 100%);
    -webkit-mask-image: linear-gradient(90deg, #000 55%, transparent 100%);
    mask-image: linear-gradient(90deg, #000 55%, transparent 100%);
  }
  .benefits { position: absolute; left: 404px; top: 138px; width: 320px; margin: 0; padding: 0; list-style: none; font: italic 400 18px/1.32 "Lato", sans-serif; color: var(--ink); }
  .benefits li { position: relative; padding-left: 18px; margin-bottom: 6px; }
  .benefits li::before { content: ""; position: absolute; left: 0; top: 8px; width: 9px; height: 9px; border-radius: 50%; background: var(--navy); }
  .benefits strong { font: normal 700 18px "Lato", sans-serif; color: var(--red); text-transform: uppercase; }
  .badge { position: absolute; border-radius: 50%; border: 4px solid var(--white); box-shadow: 0 2px 6px rgba(0,0,0,.35); display: flex; flex-direction: column; align-items: center; justify-content: center; text-align: center; color: var(--white); font-family: "Oswald", sans-serif; text-transform: uppercase; line-height: 1.08; }
  .badge .small { font-size: 16px; font-weight: 400; }
  .badge .big { font-size: 34px; font-weight: 500; line-height: 1.05; }
  .badge-front { left: 35px; top: 339px; width: 122px; height: 122px; background: var(--red); }
  .badge-back { left: 114px; top: 276px; width: 104px; height: 104px; background: var(--navy); }
  .badge-back .small { font-size: 14px; }
  .badge-back .big { font-size: 30px; }
  .contact { position: absolute; font-family: "Oswald", sans-serif; color: var(--white); }
  .contact .call { font-size: 44px; font-weight: 500; line-height: 1; white-space: nowrap; text-transform: uppercase; }
  .contact .call-label { color: var(--red); }
  .contact .email { font: 700 20px "Lato", sans-serif; margin-top: 10px; white-space: nowrap; }
  .contact .email-label { color: var(--red); }
  .contact-front { right: 32px; top: 386px; text-align: right; }
  .contact-back { left: 31px; top: 402px; }
  .contact-back .call { font-size: 40px; }
  .contact-back .email { font-size: 18px; margin-top: 8px; }
  .back-photo { left: 0; top: 0; width: 336px; height: 206px; background: linear-gradient(180deg, #4f86c9 0%, #a9c6e6 40%, #e7e6e0 62%, #6f9a48 100%); }
  .ribbon { position: absolute; left: 0; top: 206px; width: 363px; height: 62px; background: var(--red); display: flex; align-items: center; padding-left: 22px; box-sizing: border-box; font: 500 39px/1 "Oswald", sans-serif; text-transform: uppercase; color: var(--white); white-space: nowrap; }
  .ribbon .accent { color: var(--navy); margin-left: 9px; }
  .ribbon-fold { position: absolute; left: 336px; top: 194px; width: 0; height: 0; border-left: 27px solid var(--red-dark); border-top: 12px solid transparent; }
  .stamp-box { position: absolute; left: 603px; top: 39px; width: 90px; height: 75px; border: 1px solid #b5b5b5; }
  .address-line { position: absolute; left: 422px; width: 272px; height: 0; border-top: 1px solid var(--rule); }
  .line-1 { top: 222px; }
  .line-2 { top: 261px; }
  .line-3 { top: 300px; }
</style>
</head>
<body>
<main class="stage">

  <section class="card card-front" aria-label="Postcard front">
    <div class="photo front-photo" role="img" aria-label="Photo of a large two-storey suburban house at dusk with lit windows and a green lawn"></div>
    <svg class="shape-layer" width="734" height="500" viewBox="0 0 734 500" aria-hidden="true">
      <defs>
        <linearGradient id="frontBlue" x1="0" y1="0" x2="1" y2="0">
          <stop offset="0" stop-color="#142a66"/>
          <stop offset="0.5" stop-color="#2453a8"/>
          <stop offset="1" stop-color="#142a66"/>
        </linearGradient>
      </defs>
      <path d="M0,418 C180,430 360,392 520,350 C610,328 680,322 734,326 L734,500 L0,500 Z" fill="#ffffff"/>
      <path d="M0,400 C200,412 370,370 520,330 C610,308 680,304 734,308 L734,322 C680,318 610,322 520,346 C370,386 200,428 0,416 Z" fill="var(--red)"/>
      <path d="M0,438 C200,440 380,398 520,364 C610,344 680,338 734,340 L734,500 L0,500 Z" fill="url(#frontBlue)"/>
    </svg>
    <div class="headline-band"></div>
    <h1 class="headline">Keep Harbor Homes</h1>
    <ul class="benefits">
      <li><strong>Avoid</strong> Short sale</li>
      <li><strong>Avoid</strong> Foreclosure</li>
      <li><strong>Avoid</strong> Repossession</li>
      <li><strong>Avoid</strong> Negative credit inquires and all other negative actions associated with your real estate.</li>
    </ul>
    <div class="badge badge-front">
      <span class="small">Book your</span>
      <span class="small">appointment</span>
      <span class="big">Now</span>
    </div>
    <div class="contact contact-front">
      <div class="call"><span class="call-label">Call :</span> 844-27-LUMEN</div>
      <div class="email"><span class="email-label">Email Us :</span> info@keepharborhomes.example</div>
    </div>
  </section>

  <section class="card card-back" aria-label="Postcard back">
    <div class="photo back-photo" role="img" aria-label="Photo of a white house with a foreclosure home-for-sale sign on the front lawn under a blue sky"></div>
    <div class="ribbon-fold"></div>
    <div class="ribbon">Avoid<span class="accent">Foreclosure</span></div>
    <svg class="shape-layer" width="736" height="500" viewBox="0 0 736 500" aria-hidden="true">
      <defs>
        <linearGradient id="backBlue" x1="0" y1="0" x2="1" y2="0">
          <stop offset="0" stop-color="#142a66"/>
          <stop offset="0.5" stop-color="#2453a8"/>
          <stop offset="1" stop-color="#142a66"/>
        </linearGradient>
      </defs>
      <path d="M0,356 C180,338 340,362 500,396 C600,416 680,424 736,418 L736,430 C680,436 600,430 500,410 C340,378 180,352 0,372 Z" fill="var(--red)"/>
      <path d="M0,384 C180,368 340,390 500,424 C600,444 680,452 736,446 L736,500 L0,500 Z" fill="url(#backBlue)"/>
    </svg>
    <div class="badge badge-back">
      <span class="small">Book your</span>
      <span class="small">appointment</span>
      <span class="big">Now</span>
    </div>
    <div class="contact contact-back">
      <div class="call"><span class="call-label">Call :</span> 844-27-LUMEN</div>
      <div class="email"><span class="email-label">Email Us :</span> info@keepharborhomes.example</div>
    </div>
    <div class="stamp-box"></div>
    <div class="address-line line-1"></div>
    <div class="address-line line-2"></div>
    <div class="address-line line-3"></div>
  </section>

</main>
</body>
</html>
```